Boat business cards

I'm looking for business cards with the two logos I've attached. I don't have an specific idea in mind and open to anything. All the usual info will be on the card. Name, position in company, nr, email, address, ect. The company rents out these two boats for charters and fishing.

```html
<!DOCTYPE html>
<html lang="en">
<head>
<meta charset="utf-8">
<title>Charter Business Cards</title>
<link href="https://fonts.googleapis.com/css2?family=Jost:wght@400;500&display=swap" rel="stylesheet">
<style>
  :root {
    --navy: #123a66;
    --deep: #0c2a4e;
    --ocean: #1d4f82;
    --mist: #6f7f95;
    --teal: #1fb3c2;
    --white: #ffffff;
    --frame: #9a9a9a;
    --canvas: #ffffff;
  }
  * { box-sizing: border-box; margin: 0; padding: 0; }
  html, body {
    width: 1200px; height: 504px; overflow: hidden;
    background: var(--canvas);
    font-family: "Jost", sans-serif;
  }
  .sheet {
    position: relative; width: 1200px; height: 504px;
    display: flex; align-items: center; justify-content: center; gap: 40px;
  }
  .card {
    position: relative; width: 540px; height: 309px;
    background: var(--white); border: 1px solid var(--frame); overflow: hidden;
  }
  .card-art { position: absolute; inset: 0; width: 100%; height: 100%; }
  .identity { position: absolute; left: 63px; top: 108px; }
  .identity-name {
    font-size: 25px; font-weight: 400; letter-spacing: 0.5px; color: var(--navy); line-height: 1;
  }
  .identity-name .accent { color: var(--teal); }
  .identity-role { font-size: 14px; color: var(--navy); margin-top: 4px; }
  .brand-mark {
    position: absolute; display: flex; align-items: center; gap: 6px;
    color: var(--navy); font-weight: 500;
  }
  .brand-front { right: 50px; top: 62px; font-size: 18px; }
  .brand-back { left: 50%; top: 160px; transform: translateX(-50%); font-size: 38px; white-space: nowrap; }
  .brand-dot { width: 10px; height: 10px; border-radius: 50%; background: var(--teal); }
  .contact {
    position: absolute; display: flex; align-items: center; gap: 7px;
    color: var(--white); font-size: 13.5px;
  }
  .contact svg { width: 12px; height: 12px; fill: var(--teal); flex: none; }
</style>
</head>
<body>
<main class="sheet">

  <section class="card card-front">
    <svg class="card-art" viewBox="0 0 540 309" role="img" aria-label="Deep blue ocean water photograph">
      <defs>
        <linearGradient id="oceanFront" x1="0" y1="1" x2="1" y2="0">
          <stop offset="0" stop-color="#0c2a4e"/>
          <stop offset="0.55" stop-color="#1d4f82"/>
          <stop offset="1" stop-color="#6f7f95"/>
        </linearGradient>
      </defs>
      <path class="teal-band" d="M0,148 C90,192 250,188 540,66 L540,80 C260,200 90,205 0,170 Z" fill="#1fb3c2"/>
      <path class="ocean" d="M0,168 C90,205 260,205 540,74 L540,309 L0,309 Z" fill="url(#oceanFront)"/>
      <path class="swell-line" d="M0,180 C110,212 270,200 400,140" fill="none" stroke="#ffffff" stroke-width="1.5" opacity="0.8"/>
      <line class="divider" x1="270" y1="225" x2="270" y2="275" stroke="#ffffff" stroke-width="2"/>
    </svg>

    <div class="brand-mark brand-front"><span class="brand-dot"></span>Harbor Star</div>

    <div class="identity">
      <p class="identity-name">YOUR <span class="accent">NAME</span></p>
      <p class="identity-role">Position In Company</p>
    </div>

    <div class="contact" style="left:58px; top:222px;">
      <svg viewBox="0 0 24 24"><path d="M6.6 10.8a15.1 15.1 0 0 0 6.6 6.6l2.2-2.2a1 1 0 0 1 1-.25 11.4 11.4 0 0 0 3.6.57 1 1 0 0 1 1 1V20a1 1 0 0 1-1 1A17 17 0 0 1 3 4a1 1 0 0 1 1-1h3.5a1 1 0 0 1 1 1c0 1.25.2 2.45.57 3.57a1 1 0 0 1-.25 1z"/></svg>
      XXX XXX XXX
    </div>
    <div class="contact" style="left:58px; top:257px;">
      <svg viewBox="0 0 24 24"><path d="M2 5h20v14H2zm2 2v.5l8 5 8-5V7zm0 2.8V17h16V9.8l-8 5z"/></svg>
      Youremail@mail.com
    </div>
    <div class="contact" style="left:327px; top:222px;">
      <svg viewBox="0 0 24 24"><path d="M12 2a7 7 0 0 0-7 7c0 5.2 7 13 7 13s7-7.8 7-13a7 7 0 0 0-7-7zm0 9.5A2.5 2.5 0 1 1 12 6.5a2.5 2.5 0 0 1 0 5z"/></svg>
      Your Address
    </div>
    <div class="contact" style="left:327px; top:257px;">
      <svg viewBox="0 0 24 24"><path d="M12 2a10 10 0 1 0 0 20 10 10 0 0 0 0-20zm6.9 6h-3a15.6 15.6 0 0 0-1.4-3.6A8 8 0 0 1 18.9 8zM12 4c.8 1.2 1.5 2.5 1.9 4h-3.8c.4-1.5 1.1-2.8 1.9-4zM4.3 14a8 8 0 0 1 0-4h3.4a16 16 0 0 0 0 4zm.8 2h3a15.6 15.6 0 0 0 1.4 3.6A8 8 0 0 1 5.1 16zm3-8h-3a8 8 0 0 1 4.4-3.6A15.6 15.6 0 0 0 8.1 8zM12 20c-.8-1.2-1.5-2.5-1.9-4h3.8c-.4 1.5-1.1 2.8-1.9 4zm2.3-6H9.7a14 14 0 0 1 0-4h4.6a14 14 0 0 1 0 4zm.3 5.6a15.6 15.6 0 0 0 1.4-3.6h3a8 8 0 0 1-4.4 3.6zm1.7-5.6a16 16 0 0 0 0-4h3.4a8 8 0 0 1 0 4z"/></svg>
      Your Website
    </div>
  </section>

  <section class="card card-back">
    <svg class="card-art" viewBox="0 0 540 309" role="img" aria-label="Deep blue ocean water photograph">
      <defs>
        <linearGradient id="oceanBack" x1="0" y1="0" x2="1" y2="1">
          <stop offset="0" stop-color="#1d4f82"/>
          <stop offset="0.6" stop-color="#0c2a4e"/>
          <stop offset="1" stop-color="#123a66"/>
        </linearGradient>
      </defs>
      <path class="teal-band" d="M0,140 C80,180 190,180 300,140 C400,105 470,70 540,36 L540,58 C460,95 390,135 300,160 C190,190 80,190 0,155 Z" fill="#1fb3c2"/>
      <path class="ocean" d="M0,0 L540,0 L540,30 C470,62 400,98 300,130 C190,168 80,170 0,138 Z" fill="url(#oceanBack)"/>
      <path class="swell-line" d="M380,105 C440,80 490,55 540,40" fill="none" stroke="#ffffff" stroke-width="6"/>
    </svg>

    <div class="brand-mark brand-back"><span class="brand-dot"></span>Sea Breeze</div>
  </section>

</main>
</body>
</html>
```